Acai Bowl and Coffee Van need new Menus

We currently have a basic menu that is displayed in an A3 frame. It lacks images, specifically of the Acai Bowls and is difficult to read and understand.

We need a new Acai Bowl Menu and a new Drink Menu but in a more attractive and easier to read format.
We would like images of the Acai Bowls (using Images supplied or make your own) in order to show customers what is on each bowl. Customers chose what granola they would like from the three that are available. Currently we tell customers to check the bottom of the menu as they are often unaware they get to chose.

The drink menu items are simple (we have removed smoothies from our menu entirely).
The drink menu needs to have "Chai Latte" and "Dirty Chai Latte" added as options with the same S,M,L pricing as a Latte.

I have attached images of the menus and a photo of how the menus are displayed on The Moro Cart. Also attached is photos of the Acai Bowls and other food / drink items on the menu if you wish to use them in your design. I have included the files for all of our logo variations.

Our main objective with the menu redesign is to have the menu more appealing and easier to read and understand.

Industry/Entity Type

Food and Coffee

Font styles to use
Other font styles liked:
• Orplid Pro (Fill and Shadow), Trend Sans One

Colors

Designer to choose colors to be used in the design.

Requirements
Must have
• The final design must include prices and be editable in the case of any price changes in the future.

```html
<!DOCTYPE html>
<html lang="en">
<head>
<meta charset="utf-8">
<title>The Moro Cart – Açai Bowls Menu</title>
<link rel="stylesheet" href="https://fonts.googleapis.com/css2?family=Amatic+SC:wght@400;700&display=swap">
<style>
  :root {
    --backdrop: #aaa7a8;
    --blush: #f1e0e2;
    --blush-deep: #ecd4d8;
    --wood-light: #d9c4ad;
    --wood-mid: #c9ad8f;
    --ink: #2b1f1c;
    --brand-brown: #8a6a55;
    --white: #ffffff;
    --title-shadow: #8d8584;
    --accent-tan: #b9a27c;
    --treat-dark: #6d4f42;
    --treat-light: #e7cdb8;
  }
  * { box-sizing: border-box; margin: 0; padding: 0; }
  html, body { width: 1200px; height: 1200px; overflow: hidden; }
  body {
    background: var(--backdrop);
    position: relative;
    font-family: "Amatic SC", cursive;
  }
  .menu-poster {
    position: absolute;
    left: 232px; top: 80px;
    width: 736px; height: 1039px;
    background: var(--blush);
    overflow: hidden;
  }
  .hero-photo {
    position: absolute; left: 0; top: 0;
    width: 100%; height: 580px;
    background:
      radial-gradient(circle at 23% 19%, #b86d4f 0 12%, #e9d7bd 20%, transparent 24%),
      radial-gradient(circle at 77% 19%, #b86d4f 0 12%, #e9d7bd 20%, transparent 24%),
      linear-gradient(180deg, var(--wood-mid) 0%, var(--wood-light) 55%, var(--blush) 100%);
  }
  .brand-mark {
    position: absolute;
    left: 281px; top: 51px;
    width: 176px; height: 176px;
    border-radius: 50%;
    background: var(--blush-deep);
    display: flex; align-items: center; justify-content: center;
  }
  .brand-name {
    font-family: "Amatic SC", cursive;
    font-weight: 700;
    font-size: 34px;
    color: var(--brand-brown);
    text-align: center;
    line-height: 1;
  }
  .menu-title {
    position: absolute;
    left: 0; top: 360px; width: 100%;
    text-align: center;
    font-weight: 700;
    font-size: 190px;
    line-height: 1;
    color: var(--white);
    text-shadow: 6px 6px 0 var(--title-shadow);
    letter-spacing: 2px;
  }
  .treat-photo {
    position: absolute;
    left: 386px; top: 570px;
    width: 350px; height: 437px;
    background:
      radial-gradient(ellipse at 60% 40%, var(--treat-dark) 0 22%, var(--treat-light) 38%, transparent 62%),
      linear-gradient(180deg, transparent 0%, rgba(240,226,220,0.6) 100%);
  }
  .bowls-photo {
    position: absolute;
    left: 0; top: 814px;
    width: 218px; height: 225px;
    background:
      radial-gradient(circle at 30% 30%, #d9c7a4 0 20%, transparent 45%),
      radial-gradient(circle at 80% 45%, #8c7466 0 18%, transparent 42%),
      linear-gradient(135deg, #e6d6cc 0%, var(--blush) 100%);
    opacity: 0.85;
  }
  .bowl-list {
    position: absolute;
    left: 56px; top: 596px;
    width: 520px;
    list-style: none;
  }
  .bowl-item {
    position: relative;
    height: 66px;
    color: var(--ink);
    font-weight: 700;
    font-size: 19px;
    line-height: 22px;
  }
  .bowl-item .bowl-price {
    position: absolute;
    left: 468px; top: 0;
  }
  .arrow-row {
    position: absolute;
    left: 150px; top: 976px;
  }
</style>
</head>
<body>
  <main class="menu-poster">
    <div class="hero-photo" role="img" aria-label="Two açai bowls topped with banana, strawberries, coconut, peanut butter and a chocolate slice on a wooden table"></div>

    <div class="brand-mark">
      <span class="brand-name">The Moro<br>Cart</span>
    </div>

    <h1 class="menu-title">AÇAI BOWLS</h1>

    <div class="treat-photo" role="img" aria-label="Chocolate peanut slices with crumbs"></div>
    <div class="bowls-photo" role="img" aria-label="Small açai bowls with coconut and fruit toppings"></div>

    <ul class="bowl-list">
      <li class="bowl-item">Lorem ipsum is simply dummy text of the printing and typesetting industry<br>Lorem ipsum is simply dummy text<span class="bowl-price">$27</span></li>
      <li class="bowl-item">Lorem ipsum is simply dummy text of the printing and typesetting industry<br>Lorem ipsum is simply dummy text<span class="bowl-price">$27</span></li>
      <li class="bowl-item">Lorem ipsum is simply dummy text of the printing and typesetting industry<br>Lorem ipsum is simply dummy text<span class="bowl-price">$27</span></li>
      <li class="bowl-item">Lorem ipsum is simply dummy text of the printing and typesetting industry<br>Lorem ipsum is simply dummy text<span class="bowl-price">$27</span></li>
      <li class="bowl-item">Lorem ipsum is simply dummy text of the printing and typesetting industry<br>Lorem ipsum is simply dummy text<span class="bowl-price">$27</span></li>
    </ul>

    <svg class="arrow-row" width="156" height="20" viewBox="0 0 156 20" aria-hidden="true">
      <g fill="var(--accent-tan)">
        <polygon points="16,1 16,19 0,10"/>
        <polygon points="50,1 50,19 34,10"/>
        <polygon points="84,1 84,19 68,10"/>
        <polygon points="118,1 118,19 102,10"/>
        <polygon points="152,1 152,19 136,10"/>
      </g>
    </svg>
  </main>
</body>
</html>
```